Dental Design, very professional and noticable

Tindale Ridge Dental Surgery is based in Pelican Waters. We are a fast growing dental surgery and are looking for some professional business cards to send to patients.
We would like to see a design that is Vertical and uses the colours Soft Blue, Silver, White and Black. Maybe a full blue side with moto and details on back? Any other ideas or colours that you may think will make the card look unique is fine.
We need all details on the card that are listed above

Target Market(s)

Families, Retired, Other Professionals and Businesses

Industry/Entity Type

Dental

Contact Information for Business Card

Tindale Ridge Dental Surgery
Family, Cosmetic, Preventative
Dr. Owen Castrey
Dental Surgeon
BDS (Adel) FAE FADI FICD FPFA
phone: (07)50001846
fax: (07)50002917
email: tindaleridgedental@quillpost.com
http://tindaleridgedental.com/

Logo Text

Logo styles of interest
Abstract Logo
Requirements
Must have
• Vertical, Vibrant but Professional, Rounded Edges, Logo on front and back of card (different colours on each side)
Nice to have
• One side completely blue (not sure what shade) with logo and moto on bottom
Other side white, with blue or different coloured logo with details in black and silver?
Logo should show half circle with 1 end as arrow symbolizing pelican waters canal also a magnifine glass also half circled with 1 end as arrow. Any other ideas are welcome.
Should not have
• A tooth. A smile. Toothbrush or Toothpaste. Cornered edges.

```html
<!DOCTYPE html>
<html lang="en">
<head>
<meta charset="utf-8">
<title>Tindale Ridge Dental Surgery – Business Card</title>
<link rel="stylesheet" href="https://fonts.googleapis.com/css2?family=Open+Sans:wght@400&family=Tinos&family=Yanone+Kaffeesatz:wght@500&family=Josefin+Sans:wght@400&display=swap">
<style>
  :root {
    --backdrop: #2b2b2c;
    --card-blue: #1a5ea8;
    --card-blue-glow: #3d6fbf;
    --sky: #2bb4e6;
    --mark-blue: #1f93d3;
    --white: #ffffff;
    --gold: #9c7a32;
    --gold-light: #b08b38;
    --silver: #8e8e8e;
    --faint-mark: #eee9df;
  }
  * { margin: 0; padding: 0; box-sizing: border-box; }
  html, body { width: 1200px; height: 1000px; overflow: hidden; }
  body { background: var(--backdrop); position: relative; font-family: "Open Sans", sans-serif; }

  .card {
    position: absolute; top: 186px; width: 375px; height: 660px;
    border-radius: 36px; overflow: hidden;
  }
  .card--front {
    left: 174px;
    background: radial-gradient(ellipse 170px 150px at 198px 345px, var(--card-blue-glow), var(--card-blue));
  }
  .card--back { left: 686px; background: var(--white); }

  .mark { position: absolute; border-radius: 50%; }
  .front-mark { left: 156px; top: 130px; width: 58px; height: 58px; background: var(--mark-blue); }
  .front-name {
    position: absolute; top: 198px; width: 100%; text-align: center;
    font-family: "Tinos", serif; font-size: 24px; color: var(--sky); letter-spacing: -0.3px;
  }
  .front-motto {
    position: absolute; top: 230px; width: 100%; text-align: center;
    font-size: 12.5px; color: var(--white);
  }
  .front-web {
    position: absolute; top: 622px; width: 100%; text-align: center;
    font-size: 15.5px; color: var(--white);
  }

  .back-mark { left: 158px; top: 62px; width: 62px; height: 62px; background: var(--gold); }
  .back-name {
    position: absolute; top: 136px; width: 100%; text-align: center;
    font-family: "Yanone Kaffeesatz", sans-serif; font-size: 29px; color: var(--gold);
  }
  .back-motto {
    position: absolute; top: 176px; width: 100%; text-align: center;
    font-family: "Yanone Kaffeesatz", sans-serif; font-size: 21px; color: var(--gold-light);
  }
  .doctor {
    position: absolute; top: 262px; width: 100%; text-align: center;
    font-family: "Josefin Sans", sans-serif; font-size: 24px; color: var(--gold);
  }
  .role {
    position: absolute; top: 291px; width: 100%; text-align: center;
    font-size: 13px; letter-spacing: 1px; color: var(--silver);
  }
  .credentials {
    position: absolute; top: 310px; width: 100%; text-align: center;
    font-size: 10.5px; color: var(--gold-light);
  }
  .contacts { position: absolute; left: 46px; top: 352px; list-style: none; }
  .contacts li {
    display: flex; align-items: center; height: 24px;
    font-size: 13.5px; color: var(--gold-light);
  }
  .contacts svg { width: 24px; height: 20px; margin-right: 10px; fill: var(--gold); }
  .faint-mark {
    left: 92px; top: 462px; width: 190px; height: 190px; background: var(--faint-mark);
  }
</style>
</head>
<body>
  <section class="card card--front">
    <div class="mark front-mark"></div>
    <h1 class="front-name">Tindale Ridge Dental Surgery</h1>
    <p class="front-motto">Family, Cosmetic, Preventive</p>
    <p class="front-web">www.tindaleridgedental.com</p>
  </section>

  <section class="card card--back">
    <div class="mark back-mark"></div>
    <h2 class="back-name">Tindale Ridge Dental Surgery</h2>
    <p class="back-motto">Family, Cosmetic, Preventive</p>
    <p class="doctor">Dr. Owen Castrey</p>
    <p class="role">DENTAL SURGEON</p>
    <p class="credentials">BDS (Adel) FAE FADI FICD FPFA</p>
    <ul class="contacts">
      <li><svg viewBox="0 0 24 20"><path d="M2 7c0-3 5-5 10-5s10 2 10 5v2h-5V7H7v2H2z"/><rect x="4" y="10" width="16" height="9" rx="1"/></svg>phone: (07)50001846</li>
      <li><svg viewBox="0 0 24 20"><rect x="7" y="1" width="10" height="7"/><rect x="3" y="8" width="18" height="8" rx="1"/><rect x="6" y="15" width="12" height="4" fill="#fff" stroke="#9c7a32" stroke-width="1.5"/></svg>fax: (07)50002917</li>
      <li><svg viewBox="0 0 24 20"><rect x="1" y="3" width="22" height="14"/><path d="M1 3l11 8 11-8" fill="none" stroke="#fff" stroke-width="1.5"/></svg>email: tindaleridgedental@quillpost.com</li>
      <li><svg viewBox="0 0 24 20"><g fill="none" stroke="#9c7a32" stroke-width="1.6"><circle cx="12" cy="10" r="8.5"/><ellipse cx="12" cy="10" rx="4" ry="8.5"/><path d="M3.5 10h17M5 5.5h14M5 14.5h14"/></g></svg>http://tindaleridgedental.com/</li>
    </ul>
    <div class="mark faint-mark"></div>
  </section>
</body>
</html>
```